Wine Label for a White and a Red Wine from Italy

We have a very good idea of what we want with artwork. We need you to please design a 'template' with the text so we can change out the artwork from year to year. Samples are shown of what we are looking for. We are looking for options with the two basic designs. Brand name of wine is: Valora di Castegno. Both wines are in a light green Bordeaux-style bottle (note: we don't show a light green bottle in the mockup but please remember the bottle is light green). Artwork is provided. We'd like to see either the green or blue butterfly on the white wine, the red butterfly is for the red wine. Please base the design on the attached label from Brailey and/or the attached label from Chateau Mervanges.

Target Market(s)

Millennials, women

Requirements
Must have
• The artwork (butterflies) attached.
Nice to have
• Elegant, readable fonts. Please make the text so it can be changed by the printer. Please make it so the artwork can be changed too.

```html
<!DOCTYPE html>
<html lang="en">
<head>
<meta charset="utf-8">
<title>Valora di Castegno – Barrel Select Label</title>
<link rel="stylesheet" href="https://fonts.googleapis.com/css2?family=Crimson+Text:ital@0;1&family=Montserrat:wght@400;500&family=Allura&display=swap">
<style>
  :root {
    --page: #ffffff;
    --label-edge: #c9c9c9;
    --ink: #1a1a1a;
    --ink-soft: #333333;
    --silver-dark: #b4b4b4;
    --silver-mid: #e2e2e2;
    --silver-light: #ffffff;
    --art-cream: #faf8f1;
    --art-green: #8fae5a;
    --art-deep: #3f5a34;
    --art-sand: #c9b79a;
  }
  * { margin: 0; padding: 0; box-sizing: border-box; }
  html, body {
    width: 849px;
    height: 1200px;
    overflow: hidden;
    background: var(--page);
  }
  .canvas {
    position: relative;
    width: 849px;
    height: 1200px;
    background: var(--page);
  }
  .wine-label {
    position: absolute;
    left: 120px;
    top: 562px;
    width: 630px;
    height: 325px;
    display: flex;
    border: 1px solid var(--label-edge);
    background: var(--art-cream);
  }
  .label-artwork {
    width: 185px;
    height: 100%;
  }
  .label-artwork--left {
    background:
      radial-gradient(ellipse 70px 60px at 45px 150px, var(--art-deep) 0%, rgba(63,90,52,0.6) 45%, transparent 100%),
      radial-gradient(ellipse 80px 55px at 110px 110px, rgba(143,174,90,0.85) 0%, rgba(143,174,90,0.3) 60%, transparent 100%),
      radial-gradient(ellipse 70px 50px at 70px 240px, rgba(201,183,154,0.8) 0%, transparent 100%),
      var(--art-cream);
  }
  .label-artwork--right {
    width: 180px;
    background:
      radial-gradient(ellipse 70px 60px at 70px 165px, var(--art-deep) 0%, rgba(63,90,52,0.6) 45%, transparent 100%),
      radial-gradient(ellipse 85px 60px at 110px 90px, rgba(143,174,90,0.85) 0%, rgba(143,174,90,0.3) 60%, transparent 100%),
      radial-gradient(ellipse 75px 55px at 105px 250px, rgba(201,183,154,0.8) 0%, transparent 100%),
      var(--art-cream);
  }
  .label-panel {
    width: 265px;
    height: 100%;
    background: linear-gradient(90deg,
      var(--silver-dark) 0%,
      var(--silver-mid) 14%,
      var(--silver-light) 40%,
      var(--silver-light) 60%,
      var(--silver-mid) 86%,
      var(--silver-dark) 100%);
    color: var(--ink);
    text-align: center;
    position: relative;
  }
  .brand-name {
    position: absolute;
    top: 34px;
    left: 0;
    right: 0;
    font-family: "Crimson Text", serif;
    font-style: italic;
    font-weight: 400;
    font-size: 40px;
    line-height: 1;
    letter-spacing: 0.5px;
  }
  .brand-subname {
    position: absolute;
    top: 74px;
    left: 0;
    right: 0;
    padding-left: 38px;
    font-family: "Crimson Text", serif;
    font-style: italic;
    font-size: 17px;
    line-height: 1;
  }
  .cuvee {
    position: absolute;
    top: 115px;
    left: 0;
    right: 0;
    font-family: "Montserrat", sans-serif;
    font-size: 9.5px;
    letter-spacing: 3.6px;
    font-weight: 500;
  }
  .wine-details {
    position: absolute;
    top: 160px;
    left: 0;
    right: 0;
    font-family: "Crimson Text", serif;
    font-size: 13px;
    line-height: 17px;
    color: var(--ink-soft);
  }
  .divider {
    position: absolute;
    top: 229px;
    left: 129px;
    width: 6px;
    height: 1px;
    background: var(--ink-soft);
  }
  .producer {
    position: absolute;
    top: 251px;
    left: 0;
    right: 0;
    font-family: "Montserrat", sans-serif;
    font-size: 8.5px;
    color: var(--ink-soft);
  }
  .farming-note {
    position: absolute;
    top: 270px;
    left: 0;
    right: 0;
    font-family: "Allura", cursive;
    font-size: 20px;
    line-height: 1;
  }
</style>
</head>
<body>
  <main class="canvas">
    <section class="wine-label">
      <div class="label-artwork label-artwork--left" role="img" aria-label="Painted green butterfly artwork on cream ground"></div>
      <div class="label-panel">
        <h1 class="brand-name">Valora</h1>
        <p class="brand-subname">di Castegno</p>
        <p class="cuvee">BARREL SELECT</p>
        <p class="wine-details">2018<br>Rosso<br>Piemonte, Italy</p>
        <span class="divider"></span>
        <p class="producer">Artisanlly Crafted by Cantina Sei Colli</p>
        <p class="farming-note">Sustainably Farmed</p>
      </div>
      <div class="label-artwork label-artwork--right" role="img" aria-label="Painted green butterfly artwork on cream ground"></div>
    </section>
  </main>
</body>
</html>
```